Hi Designers,

I will need 4 web pages designed. The web page looks like an App (if you click on the logo, or the icon on an iPad, it will take you to the website), but it is still a webpage.

Please check the attachment on this brief to understand what specific pages I need to be designed.

A .PSD (straight-up PhotoShop image) as final deliverable is fine, as long as you give us the exact “web color numbers”.

The design is for desktop and iPad but in a single unified web application, NOT separate web app and (native) iPad app.

Details:

Bright Harbor Policy Systems is developing a browser-based application for use on any mobile device or desktop. The app will be used by corporations to communicate with their employees regarding legal, regulatory and company requirements for conducting business. The app is known as “Workplace Guidance Hub.” When the user clicks on the icon for Workplace Guidance Hub, they will enter a site full of information that a company deems necessary for the employee to do his/her job. There are several content sections within the site, including a login page, training, policies, forms, news feeds and blogs.

The application has been built using Microsoft .NET, and fully supports CSS-type skinning; it uses traditional page layouts. We are seeking a product logo concept (image), a master application/desktop icon (image), as well as a full color scheme/theme/skin design for all areas of the application (header area, body text, menu bar, etc.) in the form of a CSS. The look should be clean, crisp and professional; nothing cartoony or whimsical. It should be easy to read and “airy”.

We have sketched prototypes for the basic application page layout that we can send as a next step of the process.
Updates

Screen shots have been uploaded to this project.  Please use them to guide your design.

Dear designers,

I apologize for the delay in providing feedback. My partners and I will provide feedback in a few days. Thank you for your patience.

Industry/Entity Type

Business

Font styles to use
Other font styles liked:
• see font on screen shots when uploaded

```html
<!DOCTYPE html>
<html lang="en">
<head>
<meta charset="utf-8">
<title>Workplace Guidance Hub – Sign In</title>
<link href="https://fonts.googleapis.com/css2?family=Source+Sans+3:wght@400;600&display=swap" rel="stylesheet">
<style>
  :root {
    --bg-center: #5d9fb5;
    --bg-mid: #2a7394;
    --bg-edge: #0b4669;
    --card: #f7f8f9;
    --card-edge: #eceeef;
    --label: #555b60;
    --input-border: #d3d6d9;
    --input-bg: #ffffff;
    --divider: #e1e3e5;
    --client-navy: #0c2f57;
    --hub-blue: #2b5f93;
    --hub-green: #7cc242;
    --btn-top: #6cb83c;
    --btn-bottom: #4a9a24;
    --btn-border: #3f8520;
    --footer-text: #e3eef3;
  }
  * { box-sizing: border-box; margin: 0; padding: 0; }
  html, body { width: 1200px; height: 801px; overflow: hidden; }
  body {
    position: relative;
    font-family: "Source Sans 3", "Myriad Pro", sans-serif;
    background: radial-gradient(ellipse 780px 620px at 600px 250px, var(--bg-center) 0%, var(--bg-mid) 55%, var(--bg-edge) 100%);
  }
  .login-card {
    position: absolute; left: 99px; top: 62px; width: 1002px; height: 655px;
    background: linear-gradient(180deg, #fbfbfc 0%, var(--card) 80%, var(--card-edge) 100%);
    border-radius: 4px;
  }
  .client-name {
    position: absolute; left: 0; right: 0; top: 87px; line-height: 32px;
    display: flex; align-items: center; justify-content: center; gap: 12px;
    font-size: 26px; font-weight: 600; color: var(--client-navy);
  }
  .client-name .mark { width: 14px; height: 14px; background: var(--client-navy); }
  .divider {
    position: absolute; height: 1px;
    background: linear-gradient(90deg, transparent, var(--divider) 20%, var(--divider) 80%, transparent);
  }
  .divider.top { left: 266px; width: 475px; top: 197px; }
  .divider.bottom { left: 282px; width: 438px; top: 480px; }
  .field-label {
    position: absolute; left: 256px; width: 120px; text-align: right;
    font-size: 15.5px; line-height: 20px; color: var(--label);
  }
  .field-input {
    position: absolute; left: 397px; width: 295px; height: 38px;
    border: 1px solid var(--input-border); border-radius: 3px;
    background: var(--input-bg);
    box-shadow: inset 0 1px 2px rgba(0,0,0,0.06);
  }
  .username-label { top: 242px; }
  .username-input { top: 233px; }
  .password-label { top: 305px; }
  .password-input { top: 296px; }
  .options {
    position: absolute; left: 408px; top: 365px; line-height: 18px;
    display: flex; align-items: center;
    font-size: 15px; color: var(--label);
  }
  .checkbox {
    width: 12px; height: 12px; border: 1px solid #9a9ea2; background: #f2f3f4;
    margin-right: 11px;
  }
  .separator { color: #b9bdc0; margin: 0 13px; }
  .sign-in {
    position: absolute; left: 605px; top: 405px; width: 87px; height: 39px;
    border: 1px solid var(--btn-border); border-radius: 3px;
    background: linear-gradient(180deg, var(--btn-top), var(--btn-bottom));
    color: #fff; font-family: inherit; font-size: 17.5px; font-weight: 600;
    letter-spacing: 0.2px;
  }
  .product-name {
    position: absolute; left: 405px; top: 520px;
    display: flex; align-items: center; gap: 14px;
  }
  .product-name .mark {
    width: 40px; height: 40px; border-radius: 50%; background: var(--hub-green);
  }
  .product-name .words {
    font-size: 22px; line-height: 29px; color: var(--hub-blue);
    text-transform: uppercase; letter-spacing: 0.3px;
  }
  .copyright {
    position: absolute; left: 0; right: 0; top: 749px; text-align: center;
    font-size: 14.5px; color: var(--footer-text); word-spacing: 2px;
  }
</style>
</head>
<body>
  <main class="login-card">
    <div class="client-name"><span class="mark"></span>Corvane Labs</div>
    <div class="divider top"></div>

    <label class="field-label username-label">Username</label>
    <div class="field-input username-input"></div>

    <label class="field-label password-label">Password</label>
    <div class="field-input password-input"></div>

    <div class="options">
      <span class="checkbox"></span>
      <span>Keep me signed in</span>
      <span class="separator">|</span>
      <span>Forgot Password?</span>
    </div>

    <button class="sign-in">SIGN IN</button>

    <div class="divider bottom"></div>

    <div class="product-name">
      <span class="mark"></span>
      <span class="words">Workplace<br>Guidance<br>Hub</span>
    </div>
  </main>

  <footer class="copyright">Copyright &copy; 2013 &nbsp;Workplace Guidance Hub. &nbsp;All rights reserved.</footer>
</body>
</html>
```